Brennick Holdings Business Cards

These are professional business cards that are for my family office.
Put fake emails and phone numbers as of now until I finalize those components. This family office controls my families investments, assets, and future. The cards should be professional.
..
.
.
.
I just uploaded another variation of a logo I would like to see as a business card to I am inbeteen which logo to use

Target Market(s)

business

Industry/Entity Type

business

Contact Information for Business Card

Professional, wealth related, finance related.

Requirements
Must have
• Logo

```html
<!DOCTYPE html>
<html lang="en">
<head>
<meta charset="UTF-8">
<title>Brennick Holdings — Business Cards</title>
<link href="https://fonts.googleapis.com/css2?family=Archivo:wght@400;600;800&display=swap" rel="stylesheet">
<style>
  :root {
    --backdrop: #d9dbde;
    --card: #ffffff;
    --card-shade: #eceef1;
    --navy: #141a2e;
    --teal: #059cb4;
    --ink: #111111;
    --white: #ffffff;
  }
  * { margin: 0; padding: 0; box-sizing: border-box; }
  html, body {
    width: 1200px; height: 780px; overflow: hidden;
    background: var(--backdrop);
    font-family: "Archivo", Arial, sans-serif;
  }
  .canvas { position: relative; width: 1200px; height: 780px; }

  .card {
    position: absolute; top: 231px;
    width: 540px; height: 318px;
    border-radius: 22px; overflow: hidden;
    background: var(--card);
    box-shadow: 0 10px 28px rgba(0,0,0,0.18);
  }
  .card--front { left: 40px; }
  .card--back { left: 620px; }

  .card__texture {
    position: absolute; inset: 0;
    background: linear-gradient(135deg, var(--card) 0%, var(--card-shade) 45%, var(--card) 70%, var(--card-shade) 100%);
  }

  /* Front */
  .front-brand {
    position: absolute; left: 0; right: 0; top: 92px;
    display: flex; flex-direction: column; align-items: center; gap: 22px;
  }
  .front-brand__circle {
    width: 86px; height: 86px; border-radius: 50%;
    border: 4px solid var(--navy);
  }
  .front-brand__name {
    font-weight: 600; font-size: 40px; letter-spacing: 3px;
    text-transform: uppercase; color: var(--navy);
  }

  /* Back */
  .accent { position: absolute; inset: 0; }
  .back-brand {
    position: absolute; left: 40px; top: 40px;
    display: flex; align-items: center; gap: 10px;
  }
  .back-brand__circle {
    width: 34px; height: 34px; border-radius: 50%;
    border: 2px solid var(--navy);
  }
  .back-brand__name {
    font-weight: 600; font-size: 18px; letter-spacing: 1.5px;
    text-transform: uppercase; color: var(--navy);
  }
  .person { position: absolute; left: 40px; top: 118px; }
  .person__name { font-weight: 800; font-size: 30px; color: var(--teal); line-height: 1.1; }
  .person__role { font-weight: 800; font-size: 24px; color: var(--ink); line-height: 1.2; margin-top: 2px; }

  .contact { position: absolute; left: 40px; top: 200px; display: flex; gap: 14px; }
  .contact__icons {
    width: 34px; padding: 8px 0; border-radius: 10px;
    background: var(--teal);
    display: flex; flex-direction: column; align-items: center; justify-content: space-around;
    height: 96px;
  }
  .contact__icons svg { width: 15px; height: 15px; }
  .contact__lines { list-style: none; font-size: 15px; line-height: 19px; color: var(--ink); }
</style>
</head>
<body>
<main class="canvas">

  <section class="card card--front" aria-label="Business card front">
    <div class="card__texture" role="img" aria-label="Soft light grey faceted background"></div>
    <div class="front-brand">
      <span class="front-brand__circle"></span>
      <span class="front-brand__name">Brennick Holdings</span>
    </div>
  </section>

  <section class="card card--back" aria-label="Business card back">
    <div class="card__texture" role="img" aria-label="Soft light grey faceted background"></div>
    <svg class="accent" viewBox="0 0 540 318" aria-hidden="true">
      <polygon points="338,0 540,0 540,120 322,72" fill="var(--teal)"/>
      <polygon points="478,132 540,146 540,318 446,318" fill="var(--teal)"/>
    </svg>

    <div class="back-brand">
      <span class="back-brand__circle"></span>
      <span class="back-brand__name">Brennick Holdings</span>
    </div>

    <div class="person">
      <p class="person__name">Adrian Kessler</p>
      <p class="person__role">Graphic Design</p>
    </div>

    <div class="contact">
      <div class="contact__icons">
        <svg viewBox="0 0 24 24" aria-hidden="true"><path fill="var(--white)" d="M6.6 10.8a15 15 0 0 0 6.6 6.6l2.2-2.2a1 1 0 0 1 1-.25 11.4 11.4 0 0 0 3.6.57 1 1 0 0 1 1 1V20a1 1 0 0 1-1 1A17 17 0 0 1 3 4a1 1 0 0 1 1-1h3.5a1 1 0 0 1 1 1c0 1.25.2 2.45.57 3.57a1 1 0 0 1-.25 1z"/></svg>
        <svg viewBox="0 0 24 24" aria-hidden="true"><g fill="none" stroke="var(--white)" stroke-width="2"><circle cx="12" cy="12" r="9"/><ellipse cx="12" cy="12" rx="4" ry="9"/><path d="M3 12h18M5 7h14M5 17h14"/></g></svg>
        <svg viewBox="0 0 24 24" aria-hidden="true"><path fill="var(--white)" d="M3 5h18v14H3z"/><path fill="none" stroke="var(--teal)" stroke-width="2" d="M3 6l9 7 9-7"/></svg>
        <svg viewBox="0 0 24 24" aria-hidden="true"><path fill="var(--white)" d="M12 2a7 7 0 0 0-7 7c0 5 7 13 7 13s7-8 7-13a7 7 0 0 0-7-7zm0 9.5A2.5 2.5 0 1 1 12 6.5a2.5 2.5 0 0 1 0 5z"/></svg>
      </div>
      <ul class="contact__lines">
        <li>014-276-5530</li>
        <li>www.brennickholdings.com</li>
        <li>hello@brennickholdings.com</li>
        <li>48 Harbor Lane, Westbrook,</li>
        <li>ST 20417</li>
      </ul>
    </div>
  </section>

</main>
</body>
</html>
```